Business Card and Stationery for Brokerage & Consulting Co.
Amber Ridge Associates, Brokerage & Consulting for the Baking Industry
Business Card and Stationery for Brokerage & Consulting Co. - Food
Creative Brief
Professional
Derek Halvorsen
Partner / Business Development
4219 W. Birchmont Ave. Long Beach, CA 90714
derek@amberridgeassociates.com

```html
<!DOCTYPE html>
<html lang="en">
<head>
<meta charset="UTF-8">
<title>Amber Ridge Associates – Business Card</title>
<link href="https://fonts.googleapis.com/css2?family=Open+Sans:wght@400;700&display=swap" rel="stylesheet">
<style>
  :root {
    --backdrop: #e9e4de;
    --card-white: #ffffff;
    --wine: #5c1f2b;
    --olive: #5e7a2c;
    --ink-grey: #6b6b6b;
    --contact-text: #f3e9ea;
  }
  * { margin: 0; padding: 0; box-sizing: border-box; }
  html, body {
    width: 1200px; height: 914px; overflow: hidden;
    background: var(--backdrop);
    font-family: "Open Sans", Arial, sans-serif;
  }
  .business-card {
    position: absolute; left: 100px; top: 171px;
    width: 1000px; height: 572px;
    background: var(--card-white);
    box-shadow: 0 10px 30px rgba(0,0,0,0.18);
    overflow: hidden;
  }
  .card-bands { position: absolute; inset: 0; }
  .brand {
    position: absolute; left: 200px; top: 92px;
    display: flex; align-items: center; gap: 16px;
  }
  .brand-dot {
    width: 46px; height: 46px; border-radius: 50%;
    background: var(--wine);
  }
  .brand-name {
    font-size: 34px; font-weight: 700; color: var(--wine);
    letter-spacing: 0.5px;
  }
  .holder { position: absolute; left: 40px; top: 226px; }
  .holder-name { font-size: 25px; font-weight: 700; color: var(--wine); }
  .holder-role { font-size: 19px; color: var(--ink-grey); margin-top: 4px; }
  .contact-list {
    position: absolute; left: 612px; top: 366px;
    list-style: none; color: var(--contact-text); font-size: 16px;
  }
  .contact-item { display: flex; align-items: flex-start; gap: 12px; margin-bottom: 9px; }
  .contact-icon { width: 22px; height: 22px; flex: none; }
  .contact-text { line-height: 22px; }
</style>
</head>
<body>
  <main class="business-card">
    <svg class="card-bands" width="1000" height="572" viewBox="0 0 1000 572" aria-hidden="true">
      <path d="M0 392 Q 560 372 1000 226 L1000 572 L0 572 Z" fill="var(--wine)"/>
      <path d="M0 372 Q 560 352 1000 204" fill="none" stroke="var(--olive)" stroke-width="7"/>
    </svg>

    <div class="brand">
      <span class="brand-dot"></span>
      <span class="brand-name">Amber Ridge Associates</span>
    </div>

    <section class="holder">
      <h1 class="holder-name">Derek Halvorsen</h1>
      <p class="holder-role">Partner / Business Development</p>
    </section>

    <ul class="contact-list">
      <li class="contact-item">
        <svg class="contact-icon" viewBox="0 0 22 22"><circle cx="11" cy="11" r="11" fill="#fff"/><path d="M11 5a4 4 0 0 0-4 4c0 3 4 8 4 8s4-5 4-8a4 4 0 0 0-4-4zm0 5.5a1.5 1.5 0 1 1 0-3 1.5 1.5 0 0 1 0 3z" fill="var(--wine)"/></svg>
        <span class="contact-text">4219 W. Birchmont Ave. Long Beach,<br>CA 90714</span>
      </li>
      <li class="contact-item">
        <svg class="contact-icon" viewBox="0 0 22 22"><circle cx="11" cy="11" r="11" fill="#fff"/><path d="M8 6l2 2-1 2c1 2 2 3 3 3l2-1 2 2-1 2c-4 0-8-4-8-8z" fill="var(--wine)"/></svg>
        <span class="contact-text">310 555-0148</span>
      </li>
      <li class="contact-item">
        <svg class="contact-icon" viewBox="0 0 22 22"><circle cx="11" cy="11" r="11" fill="#fff"/><rect x="5.5" y="7" width="11" height="8" fill="var(--wine)"/><path d="M5.5 7l5.5 4.5L16.5 7" fill="none" stroke="#fff" stroke-width="1"/></svg>
        <span class="contact-text">derek@amberridgeassociates.com</span>
      </li>
      <li class="contact-item">
        <svg class="contact-icon" viewBox="0 0 22 22"><circle cx="11" cy="11" r="11" fill="#fff"/><circle cx="11" cy="11" r="5.5" fill="none" stroke="var(--wine)" stroke-width="1.3"/><path d="M5.5 11h11M11 5.5c-2.5 3-2.5 8 0 11M11 5.5c2.5 3 2.5 8 0 11" fill="none" stroke="var(--wine)" stroke-width="1.1"/></svg>
        <span class="contact-text">www.amberridgeassociates.com</span>
      </li>
    </ul>
  </main>
</body>
</html>
```